Attention grabbing 6x9 postcard

We are looking to have an attention grabbing post card that be sent out to homeowners from our roofing company Olum Roofing. the concept is that on the front it will say something like (STOP THE KNOCKING!
Tired of roofers knocking on your door? Contact us because we value your time as much as you value the roof over your head."
Olum Roofing
OlumRoofing.com
877.612.OLUM
info@olumroofing.com

Please feel free to come up with something very creative. Once we pick the final design we will provide the copy.

```html
<!DOCTYPE html>
<html lang="en">
<head>
<meta charset="utf-8">
<title>Olum Roofing Postcard</title>
<link href="https://fonts.googleapis.com/css2?family=Jost:wght@400;500&family=Space+Mono&display=swap" rel="stylesheet">
<style>
  :root {
    --page-bg: #a3a2a3;
    --card-black: #060606;
    --back-black: #151211;
    --ink-white: #ffffff;
    --brand-gold: #e9b634;
    --brick: #8e3d2c;
    --brick-dark: #5a2a22;
    --wall-white: #d9d6d2;
    --steel: #6b7580;
    --steel-dark: #20262d;
  }
  * { margin: 0; padding: 0; box-sizing: border-box; }
  html, body { width: 1200px; height: 2323px; overflow: hidden; }
  body { background: var(--page-bg); position: relative; font-family: "Jost", sans-serif; }

  .postcard { position: absolute; left: 240px; width: 720px; height: 1080px; overflow: hidden; }
  .postcard--front { top: 52px; background: var(--card-black); }
  .postcard--back { top: 1192px; background: var(--back-black); }

  /* front */
  .front-photo {
    position: absolute; inset: 0 0 auto 0; height: 520px;
    background:
      linear-gradient(180deg, rgba(6,6,6,0) 55%, var(--card-black) 100%),
      linear-gradient(90deg, var(--brick) 0%, var(--wall-white) 20%, var(--wall-white) 32%, var(--brick-dark) 45%, #5a5f55 62%, var(--brick) 80%, #b06a52 100%);
  }
  .brand-box {
    position: absolute; left: 260px; top: 470px; width: 200px; height: 168px;
    border: 2px solid var(--ink-white); border-radius: 16px;
    display: flex; align-items: center; justify-content: center;
    background: var(--card-black);
  }
  .brand-box__name { color: var(--brand-gold); font-size: 21px; font-weight: 500; letter-spacing: 0.06em; text-transform: uppercase; }
  .headline { position: absolute; left: 0; right: 0; text-align: center; color: var(--ink-white); font-weight: 400; }
  .headline--small { top: 686px; font-size: 52px; }
  .headline--large { top: 776px; font-size: 80px; }
  .tagline { position: absolute; left: 0; right: 0; top: 962px; text-align: center; color: var(--ink-white); font-size: 27px; }

  /* back */
  .back-photo {
    position: absolute; left: 365px; top: 0; width: 355px; height: 543px;
    background: linear-gradient(180deg, var(--steel-dark) 0%, var(--steel) 35%, #c8ccd0 60%, var(--steel) 100%);
  }
  .vertical { position: absolute; top: 22px; writing-mode: vertical-rl; color: var(--ink-white); white-space: nowrap; }
  .back-title { left: 292px; font-size: 42px; letter-spacing: 0.2em; text-transform: uppercase; }
  .back-contact { left: 205px; font-family: "Space Mono", monospace; font-size: 27px; line-height: 40px; letter-spacing: 0.08em; }
  .back-email { left: 30px; top: 40px; font-family: "Space Mono", monospace; font-size: 25px; letter-spacing: 0.28em; }
  .address-lines { position: absolute; left: 0; top: 0; }
  .stamp-box { position: absolute; left: 470px; top: 870px; width: 162px; height: 162px; border: 2px solid var(--ink-white); }
</style>
</head>
<body>
  <section class="postcard postcard--front">
    <div class="front-photo" role="img" aria-label="Photo of a man knocking on the white front door of a red brick house"></div>
    <div class="brand-box"><span class="brand-box__name">Olum Roofing</span></div>
    <h1 class="headline headline--small">STOP THE</h1>
    <h2 class="headline headline--large">KNOCKING!</h2>
    <p class="tagline">Tired of roofers knocking on your door?</p>
  </section>

  <section class="postcard postcard--back">
    <div class="back-photo" role="img" aria-label="Photo of a suited arm knocking on a grey door"></div>
    <p class="vertical back-title">Olum Roofing</p>
    <p class="vertical back-contact">877.612.OLUM<br>OlumRoofing.com</p>
    <p class="vertical back-email">info@olumroofing.com</p>
    <svg class="address-lines" width="720" height="1080" viewBox="0 0 720 1080" aria-hidden="true">
      <g stroke="#ffffff" stroke-width="2">
        <line x1="97" y1="587" x2="97" y2="1032"/>
        <line x1="183" y1="587" x2="183" y2="1032"/>
        <line x1="271" y1="587" x2="271" y2="1032"/>
        <line x1="360" y1="587" x2="360" y2="1032"/>
      </g>
    </svg>
    <div class="stamp-box"></div>
  </section>
</body>
</html>
```